Business Card Design

We need a business card design for a business based in Perth Western Australia. We supply bookkeeping,office systems and procedures. This company is run by professional, vibrant woman which needs to come across when looking at this card.
This includes:
Bookkeeping,BAS,Super,Payroll,Group Certificates,Year End Preparation, Budgets,Planning
Staff training
Office Clean Up, Archiving,New Files and Systems
We would like to see designs that use the colours red mahogony(see Seal attachment), black and ivory
We want a Seal(old fashion wax seal) (see attached) with the letters TL engraved into this ,with our mission statement, 'We leave our mark of excellence'
Updates

Hi to all

Please note that Tidewell Ledgers e mail address should read:  tidewellledgers.wa@quillbox.net
Thanks

Industry/Entity Type

Fashion

Contact Information for Business Card

Tidewell Ledgers
Bookkeeping,Office Systems & Procedures
Perth WA
Freya
MOB: 0438 512 647
e mail: tidewellledgers@quillbox.net

```html
<!DOCTYPE html>
<html lang="en">
<head>
<meta charset="utf-8">
<title>Tidewell Ledgers Bookkeeping – Business Card</title>
<link rel="stylesheet" href="https://fonts.googleapis.com/css2?family=Gabriela&family=Noto+Sans:wght@400&display=swap">
<style>
  :root {
    --mahogany: #5a080b;
    --lime: #b9cc4f;
    --lime-light: #c6d65e;
    --seal-red: #c4111b;
    --seal-dark: #8e0a10;
    --ink: #111111;
    --rule-red: #6e0c10;
  }
  html, body {
    margin: 0;
    padding: 0;
    width: 1200px;
    height: 741px;
    overflow: hidden;
    background: #ffffff;
  }
  .card {
    position: relative;
    width: 1200px;
    height: 741px;
    overflow: hidden;
    background: var(--mahogany);
  }
  .card__backdrop {
    position: absolute;
    inset: 0;
  }
  .brand {
    position: absolute;
    left: 402px;
    top: 78px;
    width: 700px;
  }
  .brand__name {
    margin: 0;
    font-family: "Gabriela", Georgia, serif;
    font-weight: 400;
    font-size: 78px;
    line-height: 1;
    color: var(--ink);
    letter-spacing: 2px;
  }
  .brand__tagline {
    position: absolute;
    right: 2px;
    top: 84px;
    margin: 0;
    font-family: "Noto Sans", Arial, sans-serif;
    font-size: 30px;
    line-height: 1;
    color: var(--ink);
    letter-spacing: 1px;
  }
  .brand__rule {
    position: absolute;
    left: 3px;
    top: 124px;
    width: 695px;
    height: 3px;
    background: linear-gradient(to right, var(--ink) 0 48%, var(--rule-red) 48% 100%);
  }
  .services {
    position: absolute;
    right: 81px;
    top: 252px;
    margin: 0;
    padding: 0;
    list-style: none;
    text-align: right;
    font-family: "Noto Sans", Arial, sans-serif;
    font-size: 34px;
    line-height: 44px;
    color: var(--ink);
    letter-spacing: 1.8px;
    white-space: nowrap;
  }
  .contact {
    position: absolute;
    left: 0;
    right: 0;
    top: 668px;
    margin: 0;
    text-align: center;
    font-family: "Noto Sans", Arial, sans-serif;
    font-size: 16px;
    line-height: 1;
    color: var(--ink);
    white-space: nowrap;
  }
</style>
</head>
<body>
<main class="card">
  <svg class="card__backdrop" width="1200" height="741" viewBox="0 0 1200 741" aria-hidden="true">
    <defs>
      <radialGradient id="halftone-glow" cx="0.5" cy="0.5" r="0.5">
        <stop offset="0" stop-color="#d9c98a" stop-opacity="0.35"/>
        <stop offset="1" stop-color="#d9c98a" stop-opacity="0"/>
      </radialGradient>
      <radialGradient id="seal-fill" cx="0.42" cy="0.38" r="0.65">
        <stop offset="0" stop-color="#e0262c"/>
        <stop offset="0.6" stop-color="#c4111b"/>
        <stop offset="1" stop-color="#8e0a10"/>
      </radialGradient>
      <linearGradient id="wave-band" x1="0" y1="0" x2="1" y2="0">
        <stop offset="0" stop-color="#a88a3a" stop-opacity="0"/>
        <stop offset="0.5" stop-color="#a88a3a" stop-opacity="0.35"/>
        <stop offset="1" stop-color="#a88a3a" stop-opacity="0.15"/>
      </linearGradient>
    </defs>
    <path d="M481 0 C330 90 240 250 245 420 C250 560 340 660 478 741 L1200 741 L1200 0 Z" fill="var(--lime)"/>
    <ellipse role="img" aria-label="Soft dot texture" cx="380" cy="400" rx="300" ry="230" fill="url(#halftone-glow)"/>
    <path role="img" aria-label="Flowing gold line ribbon" d="M380 700 C600 640 800 560 1200 520 L1200 575 C850 600 640 660 420 720 Z" fill="url(#wave-band)"/>
    <rect x="0" y="643" width="1200" height="49" fill="var(--lime-light)"/>
    <circle role="img" aria-label="Red wax seal" cx="238" cy="175" r="138" fill="url(#seal-fill)"/>
  </svg>

  <header class="brand">
    <h1 class="brand__name">Tidewell Ledgers</h1>
    <p class="brand__tagline">Bookkeeping</p>
    <div class="brand__rule"></div>
  </header>

  <ul class="services">
    <li>Bookkeeping,</li>
    <li>BAS,Super,Payroll,Group Certificates,</li>
    <li>Year End Preparation,</li>
    <li>Budgets,Planning</li>
    <li>Staff training</li>
    <li>Office Clean Up,</li>
    <li>Archiving,New Files and Systems</li>
  </ul>

  <p class="contact">Tidewell Ledgers Bookkeeping,Office Systems &amp; Procedures Perth WA Freya MOB: 0438 512 647 email: tidewellledgers.wa@quillbox.net</p>
</main>
</body>
</html>
```